Stratgem 840 practise with the goal to have business and people empowered by the cloud

We need a logo design for business cards for a company based in Australia Called DUVOrbaLex. We specialise in cloud tech from th full Calventra stack. i would like it to be close to calventra colours and we specilise in Calventra Stratagem 840 Client Bondwork. the design should display the confidence an security of a cloud based company. the tag line of Empowered by the cloud in the company motto.

Target Market(s)

I am targeting small to medium business up to 250 staff. i do work for not for profit and standard business.

Industry/Entity Type

Professional Service

Contact Information for Business Card

DUVOrbaLex Pty Ltd
A.C.N. 47 918 264 530
PO Box 817
Tallowmere 4287
Mobile: 0499382057
Email: Bertram@DuvorbaLex.com.au

Font styles to use
Sans Serif

Colors

Designer to choose colors to be used in the design.

Requirements
Must have
• as a cloud based business it needs to have the this as the main theme. the tag line of Empoweredby the cloud should show we look at empowering business to get the most out of the cloud to minimise the spend they have as the target for the business is business and not for profits who need the make the most of their spend.
• the attached pictures are to be a source of insperation and key areas
Nice to have
• Calventra Stratagem 840 is the core product that we sell and implentent for our clients so the theme should complement the Calventra Stratagem theme

```html
<!DOCTYPE html>
<html lang="en">
<head>
<meta charset="utf-8">
<title>DUVOrbaLex Pty Ltd — Business Card</title>
<link href="https://fonts.googleapis.com/css2?family=Open+Sans:wght@300;400;600;700&display=swap" rel="stylesheet">
<style>
  :root {
    --navy: #232a4e;
    --white: #ffffff;
    --backdrop: #e9e7e3;
    --card-shadow: rgba(20, 24, 45, 0.18);
  }
  * { box-sizing: border-box; margin: 0; padding: 0; }
  html, body {
    width: 1200px; height: 891px; overflow: hidden;
    background: var(--backdrop);
    font-family: "Open Sans", Arial, sans-serif;
  }
  .stage {
    width: 1200px; height: 891px;
    display: flex; align-items: center; justify-content: center; gap: 60px;
  }
  .card {
    width: 525px; height: 300px; position: relative;
    box-shadow: 0 10px 30px var(--card-shadow);
    overflow: hidden;
  }
  .card--front { background: var(--navy); color: var(--white); }
  .card--back { background: var(--white); color: var(--navy); }

  .brand {
    position: absolute; left: 70px; top: 100px;
    display: flex; align-items: center; gap: 18px;
  }
  .brand__square { width: 56px; height: 56px; background: var(--white); }
  .brand__name { font-weight: 300; font-size: 44px; letter-spacing: 1px; line-height: 1; }
  .brand__suffix {
    position: absolute; right: 60px; top: 178px;
    font-weight: 300; font-size: 34px; letter-spacing: 1px;
  }

  .back__block {
    position: absolute; left: 0; top: 0; width: 215px; height: 300px;
    background: var(--navy);
  }
  .contact { position: absolute; left: 255px; top: 48px; }
  .contact__name { font-weight: 700; font-size: 22px; letter-spacing: 1px; }
  .contact__title { font-weight: 600; font-size: 13px; margin-top: 2px; }
  .contact__list { list-style: none; margin-top: 30px; font-size: 14px; line-height: 1.35; }
  .contact__item { display: flex; gap: 10px; align-items: flex-start; margin-bottom: 10px; }
  .contact__icon { width: 15px; height: 15px; flex: none; margin-top: 2px; }
</style>
</head>
<body>
<main class="stage">
  <section class="card card--front" aria-label="Card front">
    <div class="brand">
      <span class="brand__square"></span>
      <span class="brand__name">DUVOrbaLex</span>
    </div>
    <span class="brand__suffix">Pty Ltd</span>
  </section>

  <section class="card card--back" aria-label="Card back">
    <div class="back__block"></div>
    <div class="contact">
      <p class="contact__name">YOUR name</p>
      <p class="contact__title">Title</p>
      <ul class="contact__list">
        <li class="contact__item">
          <svg class="contact__icon" viewBox="0 0 16 16"><path fill="var(--navy)" d="M3 1h3l1 4-2 1.5c1 2 2.5 3.5 4.5 4.5L11 9l4 1v3c0 1-1 2-2 2C7 15 1 9 1 3c0-1 1-2 2-2z"/></svg>
          <span>0499382057</span>
        </li>
        <li class="contact__item">
          <svg class="contact__icon" viewBox="0 0 16 16"><text x="0" y="13" font-size="15" font-weight="700" fill="var(--navy)" font-family="Open Sans, sans-serif">@</text></svg>
          <span>Bertram@DuvorbaLex.com.au</span>
        </li>
        <li class="contact__item">
          <svg class="contact__icon" viewBox="0 0 16 16"><path fill="none" stroke="var(--navy)" stroke-width="1.6" d="M8 15s-5-5-5-9a5 5 0 0 1 10 0c0 4-5 9-5 9z"/><circle cx="8" cy="6" r="1.8" fill="var(--navy)"/></svg>
          <span>A.C.N. 47 918 264 530<br>PO Box 817<br>Tallowmere 4287</span>
        </li>
      </ul>
    </div>
  </section>
</main>
</body>
</html>
```